"Stripper play" Poster Project!

We need a poster design for a comedy theatre production of Copper Kettle Tango by Rob Pettigrew.

It will be printed in poster sizes from A2 to A6 and should resolve well at these sizes.

The play centres around 4 girls on a 'hen party' who visit a male strip bar and meet 4 strippers.

Full synopsis:
"The story revolves around a hen night, with the bride to be heavily pregnant. Secrets start to emerge which will affect them all.

A group of male strippers are getting ready for their act, but with two new members, rehearsals are not going too well. Also the new members have not told their families what they are doing over the summer!

When they are well through their routine and have almost revealed everything, one of the guys is recognised by his girl friend and the worlds of hen night and strippers collide……!"

The final design will have to include the text in the attached file.

We would like to see bright/contrasting colours with a clear title and booking details.
Updates

I have added an image of a male 'stripper' for inspiration!

Also 2 bold/colourful images.  Feel free to use if you wish but do not feel restricted by these.

Payment is now committed.  Please continue to submit designs/amendments so the money goes to the correct designer.

Target Market(s)

Mostly females aged 18-50. Think Norman Fitch meets Blackpool!

Industry/Entity Type

Group

Requirements
Must have
• All text included in the attached file.

Nice to have
• Something that catches the viewers eye... it is a play about strippers after all!
Should not have
• Any full nudity

```html
<!DOCTYPE html>
<html lang="en">
<head>
<meta charset="utf-8">
<title>Copper Kettle Tango – Harbourside Footlights</title>
<link rel="stylesheet" href="https://fonts.googleapis.com/css2?family=Poppins:wght@600;700&family=Montserrat:wght@800&family=Lora:ital,wght@1,700&family=Tinos&display=swap">
<style>
  :root {
    --bg-core: #5a1240;
    --bg-mid: #2e0820;
    --bg-edge: #050104;
    --info-text: #d9c8d2;
    --info-shadow: #8a1d55;
    --title-fill: #f3a6d8;
    --title-stroke: #6e0f2c;
    --title-glow: #ff5fc0;
    --accent: #9b1f52;
    --accent-soft: #8a2a5c;
    --figure: #c85a9e;
    --white: #ffffff;
  }
  * { margin: 0; padding: 0; box-sizing: border-box; }
  html, body { width: 1200px; height: 849px; overflow: hidden; background: var(--bg-edge); }
  .poster {
    position: relative;
    width: 1200px;
    height: 849px;
    overflow: hidden;
    background:
      radial-gradient(ellipse 620px 380px at 560px 420px, var(--bg-core) 0%, var(--bg-mid) 55%, var(--bg-edge) 100%);
    font-family: "Poppins", Arial, sans-serif;
  }
  .info {
    position: absolute;
    top: 26px;
    width: 300px;
    text-align: center;
    color: var(--info-text);
    font-weight: 700;
    font-size: 29px;
    line-height: 47px;
    text-shadow: 2px 2px 0 var(--info-shadow);
  }
  .info sup { font-size: 15px; line-height: 0; }
  .info--date { left: -2px; }
  .info--time { left: 498px; }
  .info--entry { left: 895px; }

  .presenter {
    position: absolute;
    top: 326px;
    left: 440px;
    width: 400px;
    text-align: center;
    color: var(--info-text);
    font-weight: 600;
    font-size: 27px;
  }
  .presents {
    position: absolute;
    top: 370px;
    left: 540px;
    width: 120px;
    text-align: center;
    color: var(--info-text);
    font-family: "Lora", Georgia, serif;
    font-style: italic;
    font-size: 18px;
  }
  .figure {
    position: absolute;
    left: 68px;
    top: 308px;
    width: 68px;
    height: 188px;
    border-radius: 30px 30px 12px 12px;
    background: linear-gradient(180deg, var(--figure), var(--title-stroke));
    box-shadow: 0 0 14px var(--title-glow);
  }
  .title {
    position: absolute;
    top: 398px;
    left: 145px;
    width: 940px;
    text-align: center;
    white-space: nowrap;
    font-family: "Montserrat", Arial, sans-serif;
    font-weight: 800;
    font-size: 63px;
    letter-spacing: 4px;
    color: var(--title-fill);
    -webkit-text-stroke: 3px var(--title-stroke);
    paint-order: stroke fill;
    text-shadow: 0 0 10px var(--title-glow), 0 0 22px rgba(255, 95, 192, .5);
  }
  .author {
    position: absolute;
    top: 498px;
    right: 132px;
    color: var(--info-text);
    font-weight: 700;
    font-size: 21px;
    letter-spacing: 3px;
  }
  .venue-mark {
    position: absolute;
    left: 35px;
    top: 728px;
    width: 146px;
    height: 62px;
    display: flex;
    align-items: center;
    justify-content: center;
    gap: 6px;
    color: var(--white);
    font-weight: 700;
    font-size: 13px;
    line-height: 15px;
    text-align: center;
  }
  .venue-mark .square { width: 10px; height: 10px; background: var(--accent); flex: none; }
  .venue {
    position: absolute;
    top: 748px;
    left: 230px;
    color: var(--accent);
    font-weight: 600;
    font-size: 21px;
  }
  .phone {
    position: absolute;
    top: 752px;
    left: 600px;
    color: var(--accent);
    font-weight: 700;
    font-size: 15px;
  }
  .web {
    position: absolute;
    top: 748px;
    left: 862px;
    color: var(--accent-soft);
    font-size: 18px;
    font-family: Arial, sans-serif;
  }
  .notice {
    position: absolute;
    top: 810px;
    right: 32px;
    color: var(--white);
    font-family: "Tinos", "Times New Roman", serif;
    font-size: 17px;
  }
</style>
</head>
<body>
<main class="poster">
  <div class="info info--date">October<br>15<sup>th</sup>-19<sup>th</sup>, 2013</div>
  <div class="info info--time">Show Time:<br>7.30 pm</div>
  <div class="info info--entry">Entry:<br>£7.50 to 9.50</div>

  <div class="presenter">Harbourside Footlights</div>
  <div class="presents">presents</div>

  <div class="figure" role="img" aria-label="Light-bulb silhouette of a male dancer flexing"></div>
  <h1 class="title">COPPER KETTLE TANGO</h1>
  <div class="author">by Rob Pettigrew</div>

  <div class="venue-mark"><span class="square"></span><span>Harbourside Grand</span></div>
  <div class="venue">Harbourside Grand Theatre</div>
  <div class="phone">Phone: 01632 960482</div>
  <div class="web">www.harboursidegrand.co.uk</div>
  <div class="notice">* Contains strong language and adult themes.</div>
</main>
</body>
</html>
```